Vantor PR Website

Vantor PR are a PR company with a requirement for a new website. In consultation with the client, we have defined a wireframe for a homepage to show content and functionality. A PDF of the wire frame is attached.
Current site http://www.vantor-pr.example.co.uk/
Updates
If you are using Stock Photography - please use PixHollow
Dear All
Unfortunately, my client didn't like any of the designs submitted.
I've uploaded 3 examples of the type of photography that will appear in the carousel as supplied by the client.
Target Market(s)
Business to Business/Professionals - high value clients
Number of Pages Required
1 page
Requirements
Must have
- Colour scheme is attached as a .ase file from Swatchly and can be viewed on Swatchly if you search for 'VANTOR PR Palette'
Corporate Typeface is Futura Book - use of Glyphix is OK
Current Logo to be reatainedCall 2 Action Buttons will be controlled via the CMS so a generic background may be useful for these.
Nice to have
- RSS feeds

```html
<!DOCTYPE html>
<html lang="en">
<head>
<meta charset="utf-8">
<title>Vantor PR – Home</title>
<link rel="stylesheet" href="https://fonts.googleapis.com/css2?family=Jost:wght@400;500&family=Open+Sans:wght@400;700&display=swap">
<style>
:root{
  --teal-dark:#0f5b6e;
  --teal:#1a6f82;
  --teal-light:#a8ddd7;
  --teal-pale:#bfe6e1;
  --ink:#111;
  --white:#fff;
  --box-border:#bdbdbd;
  --btn-text:#9fdcde;
}
*{margin:0;padding:0;box-sizing:border-box}
html,body{width:1183px;height:1200px;overflow:hidden;background:var(--white)}
body{position:relative;font-family:"Open Sans",Verdana,sans-serif;color:var(--ink)}
.abs{position:absolute}
.brand{left:95px;top:26px;font-family:"Jost",sans-serif;font-size:42px;letter-spacing:5px;color:var(--teal-dark);font-weight:400;line-height:1}
.contact-links{right:80px;top:24px;display:flex;gap:20px;align-items:center;font-family:"Jost",sans-serif}
.contact-links .label{font-family:"Open Sans",sans-serif;font-size:11px;font-weight:700;color:var(--teal-dark);letter-spacing:1px;margin-right:-10px}
.contact-links .net{font-size:17px;font-weight:500;color:var(--teal)}
.phone{right:80px;top:58px;font-family:"Jost",sans-serif;font-size:25px;color:var(--teal)}
.main-nav{left:0;top:100px;width:1183px;height:54px;background:var(--teal-dark)}
.main-nav ul{list-style:none;display:flex;align-items:center;height:54px;padding-left:134px;font-family:"Jost",sans-serif;font-size:17px;color:var(--white)}
.main-nav li{padding:0 14px;position:relative;white-space:nowrap}
.main-nav li+li::before{content:"|";position:absolute;left:-4px}
.main-nav li.home{padding:0;margin-right:14px;height:54px;width:81px;background:linear-gradient(#4a4a4a,#1d1d1d);display:flex;align-items:center;justify-content:center}
.main-nav li.home::after{content:"";position:absolute;bottom:-9px;left:31px;border:9px solid transparent;border-bottom:0;border-top-color:#1d1d1d}
.main-nav li.home+li::before{content:none}
.hero{left:0;top:154px;width:1183px;height:277px;background:linear-gradient(90deg,var(--teal-light),var(--teal-pale) 40%,var(--teal-light))}
.hero-services{left:98px;top:22px;list-style:none;font-family:"Jost",sans-serif;font-size:25px;color:var(--teal-dark);line-height:50px}
.hero-photo{left:438px;top:0;width:667px;height:277px;background:linear-gradient(90deg,#e6e2dc,#6c6460 40%,#2a2a2e 70%,#c9c4be);border-radius:40px 0 0 40px/280px 0 0 280px;border-left:3px solid var(--white)}
.welcome{left:98px;top:466px;font-family:"Jost",sans-serif;font-size:37px;color:var(--teal-dark);font-weight:400;line-height:1.2}
.intro{left:98px;top:532px;width:620px;font-size:12.5px;line-height:19px}
.intro p{margin-bottom:18px}
.card{top:738px;width:287px;height:218px;border:1px solid var(--box-border);border-radius:5px;background:linear-gradient(#fff,#dcdcdc);padding:20px 16px}
.card h2{font-family:"Jost",sans-serif;font-size:24px;font-weight:400;margin-bottom:16px}
.card p{font-size:12.5px;line-height:15px;margin-bottom:14px;padding-left:2px}
.card.news{left:96px}
.card.blog{left:434px}
.blog-photo{position:absolute;right:22px;top:48px;width:81px;height:85px;background:linear-gradient(#d8d2c8,#8a7a6a)}
.blog p.short{width:155px}
.divider{border-left:1px dotted #aaa}
.cta-col{left:827px;top:475px;width:243px}
.chevron{display:block;margin:0 auto 3px}
.cta{display:flex;align-items:center;justify-content:center;height:69px;margin-bottom:14px;border:4px solid #0a0a0a;background:linear-gradient(#2a8a9e,#0c5467);font-family:"Jost",sans-serif;font-size:35px;color:var(--btn-text)}
.site-footer{left:0;top:1008px;width:1183px;height:149px;background:var(--teal-light)}
.foot-links{list-style:none;font-size:11.5px;font-weight:700;color:var(--teal-dark);line-height:19px;letter-spacing:.6px}
.signup{left:842px;top:18px}
.signup h3{font-family:"Open Sans",sans-serif;font-size:22px;font-weight:700;color:var(--teal-dark);margin-bottom:10px}
.signup .field{width:236px;height:35px;border:1px solid var(--teal-dark);background:var(--white);font-size:12px;font-weight:700;color:var(--teal-dark);padding:9px 8px;letter-spacing:.6px}
.signup .btn{margin-top:12px;width:107px;height:26px;border-radius:3px;background:linear-gradient(#2a8a9e,#0c5467);color:var(--white);font-family:"Jost",sans-serif;font-size:18px;display:flex;align-items:center;justify-content:center}
.legal{left:0;top:1157px;width:1183px;height:43px;background:var(--teal-dark);color:var(--white);font-size:11.5px;font-weight:700;letter-spacing:.6px;text-align:right;padding:10px 80px 0 0}
</style>
</head>
<body>
<header>
  <div class="abs brand">Vantor PR</div>
  <div class="abs contact-links">
    <span class="label">Email Us:</span>
    <span class="net">Ringvale</span>
    <span class="net">Chirrup</span>
    <span class="net">Chatterbox</span>
  </div>
  <div class="abs phone">Call us now 0141 555 0199</div>
</header>
<nav class="abs main-nav">
  <ul>
    <li class="home">Home</li>
    <li>Vantor Services</li>
    <li>Press Office</li>
    <li>Vantor Case Studies</li>
    <li>Vantor People</li>
    <li>Blog</li>
    <li>Vantor News</li>
    <li>Contact Us</li>
  </ul>
</nav>
<section class="abs hero">
  <ul class="abs hero-services">
    <li>Online Public Relations</li>
    <li>Media Relations</li>
    <li>Consumer Campaigns</li>
    <li>Crisis Public Relations</li>
    <li>Internal Communications</li>
  </ul>
  <div class="abs hero-photo" role="img" aria-label="Carousel photo of a smiling team of young business professionals"></div>
</section>
<main>
  <h1 class="abs welcome">Welcome to Vantor PR</h1>
  <div class="abs intro">
    <p>Vantor Public Relations is one of Scotland’s leading independent agencies. Founded in 2000, we were determined to create a public relations service with a real difference – hence the name.</p>
    <p>Vantor Public Relation's trademark is a fresh, creative and hard working approach to public relations. It is an approach that secures real results for our clients.</p>
    <p>We are an agency with intelligence, integrity and imagination offering a comprehensive, results driven public relations service covering traditional and online public relations strategy and support.</p>
  </div>
  <article class="abs card news">
    <h2>Client News</h2>
    <p>Phasellus sapien ipsum, interdum ut dapibus in, hendrerit nec nulla. Donec</p>
    <p>egestas scelerisque metus, nec placeratlectus ultrices ac. Nam sodales mollis euismod. Mauris ornare viverra dignissim.</p>
  </article>
  <div class="abs divider" style="left:408px;top:732px;height:238px"></div>
  <article class="abs card blog">
    <h2>Blog Entry</h2>
    <div class="blog-photo" role="img" aria-label="Blog author portrait"></div>
    <p class="short">Phasellus sapien ipsum, interdum ut dapibus in, hendrerit nec nulla Donec.</p>
    <p>egestas scelerisque metus, nec placeratlectus ultrices ac. Nam sodales mollis euismod. Mauris ornare viverra dignissim.</p>
  </article>
  <div class="abs divider" style="left:761px;top:475px;height:500px"></div>
  <aside class="abs cta-col">
    <svg class="chevron" width="24" height="32" viewBox="0 0 24 32"><path d="M2 2l10 9 10-9v7l-10 9-10-9z M2 14l10 9 10-9v7l-10 9-10-9z" fill="#8a8a8a"/></svg>
    <div class="cta">C2A Button</div>
    <svg class="chevron" width="24" height="32" viewBox="0 0 24 32"><path d="M2 2l10 9 10-9v7l-10 9-10-9z M2 14l10 9 10-9v7l-10 9-10-9z" fill="#8a8a8a"/></svg>
    <div class="cta">C2A Button</div>
    <svg class="chevron" width="24" height="32" viewBox="0 0 24 32"><path d="M2 2l10 9 10-9v7l-10 9-10-9z M2 14l10 9 10-9v7l-10 9-10-9z" fill="#8a8a8a"/></svg>
    <div class="cta">C2A Button</div>
    <svg class="chevron" width="24" height="32" viewBox="0 0 24 32"><path d="M2 2l10 9 10-9v7l-10 9-10-9z M2 14l10 9 10-9v7l-10 9-10-9z" fill="#8a8a8a"/></svg>
    <div class="cta">C2A Button</div>
  </aside>
</main>
<footer>
  <div class="abs site-footer">
    <ul class="abs foot-links" style="left:108px;top:26px">
      <li>Online Public Relations</li>
      <li>Media Relations</li>
      <li>Consumer Campaigns</li>
      <li>Crisis Public Relations</li>
      <li>Internal Communications</li>
    </ul>
    <ul class="abs foot-links" style="left:366px;top:26px">
      <li>Subscribe to RSS Feed</li>
      <li>Our Chatterbox page</li>
      <li>Link Three</li>
      <li>Link Four</li>
    </ul>
    <div class="abs signup">
      <h3>E-News Sign-up</h3>
      <div class="field">Email Address</div>
      <div class="btn">Subscribe</div>
    </div>
  </div>
  <div class="abs legal">© Copyright Notice | Site Credit | Legal</div>
</footer>
</body>
</html>
```